Book writer needs a Book Cover Design for 'Nuclear Weapons and International Law'

A Book Cover Design is required for a new book with a current working title of: 'Nuclear Weapons and International Law' plus subtitle something like: 'from the Harbour Atomic Conflict Assembly via the Global Bench of Equity Advisory Opinion to contemporary developments'.

The book will be issued in three formats: hardback, paperback, and electronic.

The Editor of the book is Malcolm Ferrisby.

The finished size of the paperback front cover will be 15.2mm x 22.9mm. Initial thoughts about themes for the front cover include a nuclear explosion, and perhaps scales of justice, but designers have total freedom to propose ideas.

The back cover will have approximately 250 words of text, and a space at the bottom of about 37mm for publisher logo and ISBN barcode, The designer is free to suggest anything for the back cover.

No illustrations where the copyright is owned by someone else should be used, and the designer must be able to transfer exclusive copyright in the design to the client. The designer will be acknowledged in the book (unless the designer does not want to be).

The themes in the book are:
1. Harbour Atomic conflict Assembly
2. Planet Bench Initiative
3. Global Bench of Equity Advisory Opinion
4. Dissenting Judgment By Judge Kolvaradine
5. Contemporary Activities (e.g. current case involving the Marshall Islands)

Target Market(s)

government decision makers taking decisions about nuclear weapons,iInternational lawyers, students of public international law,

Font styles to use
Serif

Requirements
Must have
• this is in the discretion of the designer
• Title, subtitle, editor (Malcolm Ferrisby)
Nice to have
• possibly images of nuclear explosion, effects of nuclear weapons, symbols for international law
Should not have
• in the discretion of the designer

```html
<!DOCTYPE html>
<html lang="en">
<head>
<meta charset="utf-8">
<title>Nuclear Weapons and International Law — Cover</title>
<link rel="stylesheet" href="https://fonts.googleapis.com/css2?family=Oranienbaum&family=Crimson+Pro:wght@600;700&family=Cinzel:wght@400&display=swap">
<style>
  :root {
    --cover-black: #000000;
    --title-white: #ffffff;
    --body-yellow: #f2d21e;
    --subtitle-gold: #e0a93a;
    --emblem-sky: #bfe0f2;
    --emblem-gold: #e9c33a;
    --emblem-olive: #6d5b14;
  }
  * { margin: 0; padding: 0; box-sizing: border-box; }
  html, body { width: 1200px; height: 875px; overflow: hidden; background: var(--cover-black); }
  .cover { position: relative; width: 1200px; height: 875px; background: var(--cover-black); overflow: hidden; }

  .title-type {
    font-family: "Oranienbaum", "Bodoni Moda", serif;
    font-weight: 400;
    fill: var(--title-white);
  }

  .back-title { position: absolute; left: 48px; top: 40px; width: 500px; height: 46px; }
  .blurb {
    position: absolute; left: 48px; top: 92px; width: 500px;
    font-family: "Crimson Pro", Georgia, serif;
    font-weight: 700;
    color: var(--body-yellow);
    font-size: 14.2px;
    line-height: 19.3px;
  }
  .blurb p { margin-bottom: 19.3px; }
  .blurb p.list-intro { margin-bottom: 0; }
  .theme-list { list-style: none; }

  .front-cover { position: absolute; left: 600px; top: 0; width: 600px; height: 875px; }
  .front-title { position: absolute; left: 0; top: 30px; width: 600px; height: 250px; }
  .subtitle {
    position: absolute; left: 75px; width: 480px; top: 286px;
    text-align: center;
    font-family: "Crimson Pro", Georgia, serif;
    font-weight: 600;
    font-variant: small-caps;
    color: var(--subtitle-gold);
    font-size: 18.5px;
    line-height: 21px;
    letter-spacing: 0.3px;
    white-space: nowrap;
  }
  .emblem { position: absolute; left: 193px; top: 497px; width: 240px; height: 240px; }
  .editor {
    position: absolute; left: 12px; width: 600px; top: 792px;
    text-align: center;
    font-family: "Cinzel", "Trajan Pro", serif;
    color: var(--title-white);
    font-size: 28px;
    letter-spacing: 1px;
  }
</style>
</head>
<body>
<main class="cover">
  <section class="back-cover">
    <svg class="back-title" viewBox="0 0 500 46" aria-labelledby="back-title-text">
      <text id="back-title-text" class="title-type" x="2" y="35" font-size="44" textLength="482" lengthAdjust="spacingAndGlyphs">NUCLEAR WEAPONS AND INTERNATIONAL LAW</text>
    </svg>
    <div class="blurb">
      <p>A Book Cover Design is required for a new book with a current working title of: 'Nuclear Weapons and International Law' plus subtitle something like: 'from the Harbour Atomic Conflict Assembly via the Global Bench of Equity Advisory Opinion to contemporary developments'.</p>
      <p>The book will be issued in three formats: hardback, paperback, and electronic.</p>
      <p>The Editor of the book is Malcolm Ferrisby.</p>
      <p>The finished size of the paperback front cover will be 15.2mm x 22.9mm. Initial thoughts about themes for the front cover include a nuclear explosion, and perhaps scales of justice, but designers have total freedom to propose ideas.</p>
      <p>The back cover will have approximately 250 words of text, and a space at the bottom of about 37mm for publisher logo and ISBN barcode, The designer is free to suggest anything for the back cover.</p>
      <p>No illustrations where the copyright is owned by someone else should be used, and the designer must be able to transfer exclusive copyright in the design to the client. The designer will be acknowledged in the book (unless the designer does not want to be).</p>
      <p class="list-intro">The themes in the book are:</p>
      <ol class="theme-list">
        <li>1. Harbour Atomic conflict Assembly</li>
        <li>2. Planet Bench Initiative</li>
        <li>3. Global Bench of Equity Advisory Opinion</li>
        <li>4. Dissenting Judgment By Judge Kolvaradine</li>
        <li>5. Contemporary Activities (e.g. current case involving the Marshall Islands)</li>
      </ol>
    </div>
  </section>

  <section class="front-cover">
    <svg class="front-title" viewBox="0 0 600 250" role="heading" aria-level="1" aria-label="Nuclear Weapons and International Law">
      <text class="title-type" x="308" y="85" font-size="108" text-anchor="middle" textLength="464" lengthAdjust="spacingAndGlyphs">NUCLEAR WEAPONS</text>
      <text class="title-type" x="307" y="148" font-size="55" text-anchor="middle" textLength="55" lengthAdjust="spacingAndGlyphs">AND</text>
      <text class="title-type" x="312" y="238" font-size="101" text-anchor="middle" textLength="468" lengthAdjust="spacingAndGlyphs">INTERNATIONAL LAW</text>
    </svg>
    <p class="subtitle">from the Harbour Atomic Conflict Assembly via<br>The Global Bench of Equity Advisory<br>Opinion to contemporary developments</p>
    <svg class="emblem" viewBox="0 0 240 240" role="img" aria-label="Circular emblem illustration: seated figure of justice with scales above twin globes and laurel branches on a sunburst">
      <defs>
        <radialGradient id="emblem-fill" cx="50%" cy="40%" r="60%">
          <stop offset="0%" stop-color="#e9c33a"/>
          <stop offset="55%" stop-color="#bfe0f2"/>
          <stop offset="100%" stop-color="#ffffff"/>
        </radialGradient>
      </defs>
      <circle cx="120" cy="120" r="118" fill="url(#emblem-fill)" stroke="#6d5b14" stroke-width="3"/>
    </svg>
    <p class="editor">Malcolm Ferrisby</p>
  </section>
</main>
</body>
</html>
```